Webbanner-Design für Fachhandel für Medizinprodukte
Zielgruppe
wir sind ein Fachhandel für Medizinprodukte.
Aufgabenstellung
-Slider / Banner
-1920 x 340
-Es muss ein intersannter Satz auf dem Bild sein, der einläd zu klicken.
-https://www.veloquar-beispiel.de/
- folgender Artikel soll beworben werden:
-https://www.veloquar-beispiel.de/fingerpulsoximeter-kt508-pulsoximeter-weiss-4186
-Design soll gut zur Seite passen.
-Das Bild kann von der Seite verwendet werden.
-Gerne können zusätzlich auch Stockbilder verarbeitet werden.

```html
<!DOCTYPE html>
<html lang="de">
<head>
<meta charset="utf-8">
<title>Entspannt messen – Webbanner</title>
<link href="https://fonts.googleapis.com/css2?family=Arimo:wght@700&display=swap" rel="stylesheet">
<style>
  :root {
    --stage: #9ca1a5;
    --green: #43ae4a;
    --ink: #262626;
    --paper: #e1e1e1;
    --white: #ffffff;
    --divider: #c6c6c6;
    --product: #ececec;
    --product-edge: #d2d2d2;
  }
  html, body {
    margin: 0;
    padding: 0;
    width: 1200px;
    height: 1200px;
    overflow: hidden;
    background: var(--stage);
  }
  .stage {
    position: relative;
    width: 1200px;
    height: 1200px;
  }
  .banner {
    position: absolute;
    left: 76px;
    width: 1048px;
    height: 185px;
    filter: drop-shadow(38px 34px 16px rgba(40, 42, 45, 0.85));
  }
  .banner svg { display: block; width: 1048px; height: 185px; }
  .banner--dark-wedge { top: 155px; }
  .banner--circles { top: 523px; }
  .banner--triangles { top: 887px; }
  .headline {
    font-family: "Arimo", Arial, sans-serif;
    font-weight: 700;
    font-size: 82px;
  }
  .headline--white { fill: var(--white); }
  .headline--green { fill: var(--green); }
  .headline--ink { fill: var(--ink); }
  .product-shot { fill: var(--product); stroke: var(--product-edge); stroke-width: 1; }
  .plus-badge rect { fill: var(--green); }
  .plus-badge path { fill: var(--white); }
</style>
</head>
<body>
<main class="stage">

  <!-- Banner: green field with dark wedge -->
  <section class="banner banner--dark-wedge">
    <svg viewBox="0 0 1048 185" aria-label="Entspannt messen">
      <rect width="1048" height="185" fill="var(--green)"/>
      <polygon points="0,115 815,180 1048,132 1048,185 0,185" fill="var(--ink)"/>
      <g role="img" aria-label="Produktfoto: Fingerpulsoximeter, aufrecht stehend">
        <rect class="product-shot" x="88" y="22" width="104" height="148" rx="18" transform="rotate(-14 140 96)"/>
      </g>
      <g role="img" aria-label="Produktfoto: weißes Fingerpulsoximeter mit Display">
        <rect class="product-shot" x="246" y="25" width="187" height="143" rx="14"/>
      </g>
      <g class="plus-badge" transform="translate(6 160)">
        <rect width="20" height="20" rx="4"/>
        <path d="M8 4h4v4h4v4h-4v4H8v-4H4V8h4z"/>
      </g>
      <text class="headline headline--white" x="542" y="71" textLength="460" lengthAdjust="spacingAndGlyphs">ENTSPANNT</text>
      <text class="headline headline--ink" x="542" y="146" textLength="317" lengthAdjust="spacingAndGlyphs">MESSEN</text>
    </svg>
  </section>

  <!-- Banner: light field with circles -->
  <section class="banner banner--circles">
    <svg viewBox="0 0 1048 185" aria-label="Entspannt messen">
      <defs><clipPath id="clip-circles"><rect width="1048" height="185"/></clipPath></defs>
      <rect width="1048" height="185" fill="var(--paper)"/>
      <g clip-path="url(#clip-circles)">
        <circle cx="716" cy="145" r="93" fill="var(--ink)"/>
        <circle cx="868" cy="89" r="146" fill="var(--green)"/>
        <circle cx="986" cy="191" r="43" fill="var(--ink)"/>
      </g>
      <g role="img" aria-label="Produktfoto: weißes Fingerpulsoximeter mit Display">
        <rect class="product-shot" x="772" y="24" width="190" height="142" rx="14"/>
      </g>
      <text class="headline headline--green" x="22" y="81" textLength="458" lengthAdjust="spacingAndGlyphs">ENTSPANNT</text>
      <line x1="22" y1="92" x2="480" y2="92" stroke="var(--divider)" stroke-width="2"/>
      <text class="headline headline--ink" x="22" y="160" textLength="315" lengthAdjust="spacingAndGlyphs">MESSEN</text>
      <g class="plus-badge" transform="translate(348 126) scale(1.75)">
        <rect width="20" height="20" rx="4"/>
        <path d="M8 4h4v4h4v4h-4v4H8v-4H4V8h4z"/>
      </g>
    </svg>
  </section>

  <!-- Banner: light field with triangles -->
  <section class="banner banner--triangles">
    <svg viewBox="0 0 1048 185" aria-label="Entspannt messen">
      <defs><clipPath id="clip-triangles"><rect width="1048" height="185"/></clipPath></defs>
      <rect width="1048" height="185" fill="var(--paper)"/>
      <g clip-path="url(#clip-triangles)">
        <polygon points="47,0 247,0 390,118 19,185" fill="var(--green)"/>
        <polyline points="143,0 407,76 242,185" fill="none" stroke="var(--ink)" stroke-width="1.5"/>
        <line x1="0" y1="59" x2="19" y2="185" stroke="var(--ink)" stroke-width="1.5"/>
        <line x1="22" y1="0" x2="0" y2="124" stroke="var(--green)" stroke-width="1.5"/>
        <line x1="242" y1="185" x2="404" y2="137" stroke="var(--green)" stroke-width="1.5"/>
      </g>
      <g role="img" aria-label="Produktfoto: weißes Fingerpulsoximeter mit Display">
        <rect class="product-shot" x="52" y="11" width="217" height="158" rx="16"/>
      </g>
      <text class="headline headline--green" x="523" y="81" textLength="458" lengthAdjust="spacingAndGlyphs">ENTSPANNT</text>
      <text class="headline headline--ink" x="523" y="160" textLength="315" lengthAdjust="spacingAndGlyphs">MESSEN</text>
      <g class="plus-badge" transform="translate(848 126) scale(1.75)">
        <rect width="20" height="20" rx="4"/>
        <path d="M8 4h4v4h4v4h-4v4H8v-4H4V8h4z"/>
      </g>
    </svg>
  </section>

</main>
</body>
</html>
```